Business Cards that are elegant and wow

I want to create and print business cards that represent my brand and stand out from the rest. We want to ensure they stay in our branding and the integrity is not lost. I am happy to look at different shapes like square etc.

It will be printed on very thick cards and will be stylish .

I want to create and print business cards that represent my brand and stand out from the rest. We want to ensure they stay in ur branding and the integrity is not lost. I am happy to look at different shapes like square etc.

Target Market(s)

real estate professionals

Industry/Entity Type

Real Estate

Contact Information for Business Card

Maren Holt
hello@brightfernrealty.com.au
brightfernrealty.com.au
0487 316 252 (SMS)

Colors

Designer to choose colors to be used in the design.

Requirements
Must have
• My logo
• email
• website
• Name
Nice to have
• I like the idea of printing with foil or spot gloss. You want it to stand out in a sea.
Should not have
• I would like you to stay in my colour themes. Don't change the colour of my logo

```html
<!DOCTYPE html>
<html lang="en">
<head>
<meta charset="utf-8">
<title>Maren Holt — Business Card</title>
<link rel="stylesheet" href="https://fonts.googleapis.com/css2?family=Nunito:wght@700&family=Quicksand:wght@400;500;600&display=swap">
<style>
  :root {
    --brand-pink: #e91e78;
    --brand-blue: #1dbbeb;
    --card-white: #ffffff;
    --card-edge: #2a2a2a;
  }
  * { margin: 0; padding: 0; box-sizing: border-box; }
  html, body {
    width: 1200px;
    height: 707px;
    overflow: hidden;
    background: var(--card-white);
  }
  .card {
    position: relative;
    width: 1200px;
    height: 707px;
    background: var(--card-white);
    border: 1px solid var(--card-edge);
    overflow: hidden;
  }
  .band-top {
    position: absolute;
    top: 0; left: 0; right: 0;
    height: 43px;
    background: var(--brand-pink);
  }
  .band-bottom {
    position: absolute;
    bottom: 0; left: 0; right: 0;
    height: 40px;
    background: var(--brand-blue);
  }
  .holder-name {
    position: absolute;
    left: 52px;
    top: 112px;
    font-family: "Nunito", sans-serif;
    font-weight: 700;
    font-size: 60px;
    letter-spacing: -2px;
    line-height: 1;
    color: var(--brand-blue);
  }
  .contact-list {
    position: absolute;
    left: 53px;
    top: 208px;
    list-style: none;
    font-family: "Quicksand", sans-serif;
    font-weight: 400;
    font-size: 37px;
    line-height: 56px;
    color: var(--brand-pink);
  }
  .brand-lockup {
    position: absolute;
    left: 823px;
    top: 551px;
    display: flex;
    align-items: center;
    gap: 14px;
  }
  .brand-lockup svg { display: block; flex: none; }
  .brand-name {
    font-family: "Quicksand", sans-serif;
    font-weight: 600;
    font-size: 28px;
    line-height: 32px;
    color: var(--brand-blue);
    white-space: nowrap;
  }
  .brand-name span { display: block; }
</style>
</head>
<body>
  <main class="card">
    <div class="band-top"></div>

    <h1 class="holder-name">Maren Holt</h1>

    <ul class="contact-list">
      <li class="contact-phone">tel:0487 316 252</li>
      <li class="contact-email">hello@brightfernrealty.com.au</li>
      <li class="contact-web">Brightfernrealty.com.au</li>
    </ul>

    <div class="brand-lockup">
      <svg width="80" height="80" viewBox="0 0 80 80" aria-hidden="true">
        <circle cx="40" cy="40" r="36" fill="none" stroke="var(--brand-pink)" stroke-width="6"/>
      </svg>
      <p class="brand-name"><span>BRIGHT FERN</span><span>REALTY</span></p>
    </div>

    <div class="band-bottom"></div>
  </main>
</body>
</html>
```